Limbcraft Arbor Crew Bill Board Design

We are a high class full service tree company who specializes in artistic thinning and shaping of trees in Arizona. We want to re brand our company to catch our audiences attention and hook them into calling our company on the spot. We’ve been in business for 30 years and have never truly branded our company. We want our shirts trucks and billboards to match as well as our mailing advertisement so our clientele can recognize us immediately. We are starting with our billboard first and will be following with truck and shirt designs next. Attached is a example of what we are looking for and what we’ve had designed so far. This just isn’t good enough and needs revamped if at all posssible.
- Stencil

```html
<!DOCTYPE html>
<html lang="en">
<head>
<meta charset="utf-8">
<title>Limbcraft Arbor Crew Billboard</title>
<link rel="stylesheet" href="https://fonts.googleapis.com/css2?family=Poppins:wght@800&family=Libre+Baskerville:wght@700&display=swap">
<style>
  :root {
    --navy: #10236e;
    --leaf: #45c21f;
    --grass: #12a117;
    --pill: #43b82b;
    --white: #ffffff;
    --canvas: #eef1f5;
    --photo-canopy: #5f7d4f;
    --photo-sky: #7ea6d8;
    --photo-yard: #a99a86;
  }
  html, body {
    margin: 0;
    padding: 0;
    width: 1200px;
    height: 1039px;
    overflow: hidden;
    background: var(--canvas);
  }
  .billboard {
    position: absolute;
    left: 20px;
    top: 352px;
    width: 1615px;
    height: 465px;
    transform: scale(0.7183);
    transform-origin: 0 0;
    background: var(--white);
    overflow: hidden;
  }
  .billboard-shapes {
    position: absolute;
    inset: 0;
  }
  .headline {
    position: absolute;
    left: 361px;
    width: 910px;
    margin: 0;
    font-family: "Poppins", sans-serif;
    font-weight: 800;
    font-size: 100px;
    line-height: 1;
    text-align: center;
    letter-spacing: -1px;
  }
  .headline-top { top: 38px; color: var(--white); }
  .headline-bottom { top: 124px; color: var(--leaf); }
  .tagline {
    position: absolute;
    left: 361px;
    width: 910px;
    top: 222px;
    margin: 0;
    font-family: "Libre Baskerville", serif;
    font-weight: 700;
    font-size: 46px;
    line-height: 52px;
    color: var(--white);
    text-align: center;
    text-transform: uppercase;
  }
  .phone-pill {
    position: absolute;
    left: 523px;
    top: 354px;
    width: 608px;
    height: 70px;
    border-radius: 35px;
    background: var(--pill);
    display: flex;
    align-items: center;
  }
  .phone-icon {
    width: 74px;
    height: 74px;
    margin-left: -2px;
    flex: none;
  }
  .phone-number {
    flex: 1;
    text-align: center;
    font-family: "Poppins", sans-serif;
    font-weight: 800;
    font-size: 62px;
    line-height: 1;
    color: var(--white);
    padding-right: 16px;
  }
</style>
</head>
<body>
  <div class="billboard">
    <svg class="billboard-shapes" viewBox="0 0 1615 465" width="1615" height="465">
      <defs>
        <linearGradient id="canopyTone" x1="0" y1="0" x2="1" y2="1">
          <stop offset="0" stop-color="var(--photo-sky)"/>
          <stop offset="0.5" stop-color="var(--photo-canopy)"/>
          <stop offset="1" stop-color="#4a5e3c"/>
        </linearGradient>
        <linearGradient id="yardTone" x1="0" y1="0" x2="0" y2="1">
          <stop offset="0" stop-color="var(--photo-sky)"/>
          <stop offset="0.45" stop-color="#6d8a55"/>
          <stop offset="1" stop-color="var(--photo-yard)"/>
        </linearGradient>
      </defs>
      <polygon class="photo-left" role="img" aria-label="Photo of an arborist in a bucket lift trimming a tall pine tree"
               points="0,0 333,0 420,300 375,465 0,465" fill="url(#canopyTone)"/>
      <polygon class="photo-right" role="img" aria-label="Photo of a worker tending a newly planted young tree in a gravel yard"
               points="1298,0 1615,0 1615,465 1270,465 1222,300" fill="url(#yardTone)"/>
      <polygon class="center-panel" points="361,0 1271,0 1138,465 499,465" fill="var(--navy)"/>
      <polygon class="accent-left" points="426,299 378,465 474,465" fill="var(--grass)"/>
      <polygon class="accent-right" points="1213,299 1165,465 1261,465" fill="var(--grass)"/>
    </svg>

    <h1 class="headline headline-top">LIMBCRAFT</h1>
    <p class="headline headline-bottom">ARBOR CREW</p>
    <p class="tagline">Canopy Care<br>Pros</p>

    <div class="phone-pill">
      <svg class="phone-icon" viewBox="0 0 74 74" aria-hidden="true">
        <circle cx="37" cy="37" r="34" fill="var(--pill)" stroke="var(--white)" stroke-width="5"/>
        <path d="M27 22c2-1 4 0 5 2l3 6c1 2 0 3-1 4l-2 2c2 4 5 7 9 9l2-2c1-1 3-2 4-1l6 3c2 1 3 3 2 5l-2 4c-1 2-4 3-6 2-12-4-20-12-24-24-1-2 0-5 2-6z" fill="#111"/>
        <path d="M43 24a10 10 0 0 1 8 8M44 17a17 17 0 0 1 14 14" fill="none" stroke="#111" stroke-width="3" stroke-linecap="round"/>
      </svg>
      <span class="phone-number">602-555-0148</span>
    </div>
  </div>
</body>
</html>
```